U.S. Popcorn company needs business cards

We are a popcorn company that manufactures popcorn and sells it to grocery stores worldwide. Our theme is "Americana" and our logo is U.S. route 66 which is the most famous highway in the U.S.

We would like the design to be simple and to use both sides. On the back side we would like to see just the logo and website. The front would be normal details

Target Market(s)

Wholesalers, grocers and distributors

Industry/Entity Type

Manufacture

Contact Information for Business Card

Business name: Bluebell Ridge Popcorn
Phone: +1 555 014 2286
Email: Derek@bluebellridgepopcorn.com
website: www.bluebellridgepopcorn.com
Tag Line: "Freshly popped daily"
Name: Derek Halvorsen
Title: Founder/President

Requirements
Must have
• Either this design should be fun or clean and simple. I will let you show me your thougths.
Nice to have
• Anything that ties in the real Hwy Route 66.
• Colors might need to be red, white and blue incorporated.
Should not have
• Not be too busy.

```html
<!DOCTYPE html>
<html lang="en">
<head>
<meta charset="utf-8">
<title>Bluebell Ridge Popcorn – Business Cards</title>
<link rel="stylesheet" href="https://fonts.googleapis.com/css2?family=Source+Sans+3:ital,wght@0,400;0,600;0,700;1,600&display=swap">
<style>
  :root {
    --navy: #0d2a66;
    --navy-light: #1b3d82;
    --red: #d8202a;
    --white: #ffffff;
    --ink: #4a4a4a;
    --backdrop: #e8e8e8;
    --font: "Source Sans 3", sans-serif;
  }
  * { box-sizing: border-box; margin: 0; padding: 0; }
  html, body {
    width: 1200px; height: 987px; overflow: hidden;
    background: var(--backdrop);
    font-family: var(--font);
  }
  .card {
    position: absolute; left: 293px;
    width: 615px; height: 352px;
    overflow: hidden;
  }
  .card--front { top: 130px; background: var(--white); }
  .card--back { top: 505px; background: var(--navy); }

  .band { position: absolute; left: 0; right: 0; height: 15px; background: var(--navy); }
  .band--top { top: 0; }
  .band--bottom { bottom: 0; height: 19px; }
  .dash-rule {
    position: absolute; left: 0; right: 0; height: 2px;
    background: repeating-linear-gradient(90deg, var(--red) 0 14px, transparent 14px 18px);
  }
  .dash-rule--top { top: 19px; }
  .dash-rule--bottom { bottom: 23px; }

  .brand {
    position: absolute; display: flex; flex-direction: column; align-items: center;
    text-align: center; font-weight: 700; line-height: 1.05;
  }
  .brand__dot { width: 22px; height: 22px; border-radius: 50%; background: var(--red); margin-bottom: 10px; }
  .brand__name { font-size: 26px; }
  .card--front .brand { left: 56px; top: 116px; width: 200px; color: var(--navy); }

  .divider { position: absolute; left: 268px; top: 93px; width: 1px; height: 175px; background: #cfcfcf; }

  .person { position: absolute; left: 298px; top: 112px; }
  .person__name { font-size: 23px; font-weight: 600; color: var(--navy); }
  .person__title { font-size: 16px; color: var(--red); margin-top: 2px; }

  .contacts { position: absolute; left: 298px; top: 175px; list-style: none; }
  .contacts li {
    display: flex; align-items: center; gap: 9px;
    font-size: 15.5px; color: var(--ink); height: 23.5px;
  }
  .contacts svg { width: 15px; height: 15px; fill: var(--navy); flex: none; }

  .sunburst {
    position: absolute; inset: 0;
    background: radial-gradient(circle at 50% 45%, var(--navy-light) 0%, var(--navy) 70%);
  }
  .card--back .brand { left: 0; right: 0; top: 102px; color: var(--white); }
  .card--back .brand__name { font-size: 30px; }
  .tagline {
    position: absolute; left: 0; right: 0; top: 296px; text-align: center;
    color: var(--white); font-size: 18px; font-style: italic; font-weight: 600;
  }
</style>
</head>
<body>

<section class="card card--front" aria-label="Business card front">
  <div class="band band--top"></div>
  <div class="dash-rule dash-rule--top"></div>

  <div class="brand">
    <span class="brand__dot"></span>
    <span class="brand__name">Bluebell Ridge<br>Popcorn</span>
  </div>

  <div class="divider"></div>

  <div class="person">
    <h1 class="person__name">Derek Halvorsen</h1>
    <p class="person__title">Founder/President</p>
  </div>

  <ul class="contacts">
    <li>
      <svg viewBox="0 0 24 24" aria-hidden="true"><path d="M6.6 10.8a15.1 15.1 0 0 0 6.6 6.6l2.2-2.2a1 1 0 0 1 1-.25 11.4 11.4 0 0 0 3.6.57 1 1 0 0 1 1 1V20a1 1 0 0 1-1 1A17 17 0 0 1 3 4a1 1 0 0 1 1-1h3.5a1 1 0 0 1 1 1c0 1.250.2 2.45.57 3.57a1 1 0 0 1-.25 1z"/></svg>
      +1 555 014 2286
    </li>
    <li>
      <svg viewBox="0 0 24 24" aria-hidden="true"><path d="M2 5h20v14H2z M4 7v.5l8 5 8-5V7l-8 5z" fill-rule="evenodd"/></svg>
      Derek@bluebellridgepopcorn.com
    </li>
    <li>
      <svg viewBox="0 0 24 24" aria-hidden="true"><path d="M12 2a10 10 0 1 0 0 20 10 10 0 0 0 0-20zm-1 17.9A8 8 0 0 1 4.1 11H7c.2 3.2 1.6 6.2 4 8.9zM7 9H4.3A8 8 0 0 1 11 4.1C8.6 6.8 7.2 9.1 7 9zm6 10.9c2.4-2.7 3.8-5.7 4-8.9h2.9A8 8 0 0 1 13 19.9zM17 9c-.2-1-1.6-3.2-4-4.9A8 8 0 0 1 19.7 9z"/></svg>
      www.bluebellridgepopcorn.com
    </li>
  </ul>

  <div class="dash-rule dash-rule--bottom"></div>
  <div class="band band--bottom"></div>
</section>

<section class="card card--back" aria-label="Business card back">
  <div class="sunburst" role="img" aria-label="Navy sunburst rays radiating from the centre"></div>

  <div class="brand">
    <span class="brand__dot"></span>
    <span class="brand__name">Bluebell Ridge<br>Popcorn</span>
  </div>

  <p class="tagline">Freshly popped daily</p>
</section>

</body>
</html>
```